依頼詳細
あまりゴテゴテしないデザインを希望します。
記載項目
オモテ面:ロゴ(シンボル)のみ
ウラ面 :ロゴ(タイプ)、氏名、役職、メールアドレス、電話番号、住所、HPのURL
希望イメージ
シンプル 複雑
単色 カラフル
暗い 明るい
日常 高級
遊び心 厳粛
未来的 伝統的
女性的 男性的
希望する色
青系、水色系、グレー系
納品ファイル
• イラストレーター形式 (.ai)
補足説明

オブジェクトの均等の取れた感じに好印象を抱きました。

この度は当社のコンペに多くの提案をしていただきありがとうございました。

```html
<!DOCTYPE html>
<html lang="ja">
<head>
<meta charset="utf-8">
<title>METRO CORE24 Business Card</title>
<link rel="stylesheet" href="https://fonts.googleapis.com/css2?family=Russo+One&family=Noto+Sans+JP:wght@400;500;700&family=Roboto:wght@400;500;700&display=swap">
<style>
  :root {
    --page-bg: #e9e9e9;
    --card-dark: #2a1f1f;
    --card-light: #ffffff;
    --gold: #c9a04a;
    --gold-light: #f0d891;
    --gold-deep: #8a6424;
    --ink: #222222;
    --ink-soft: #555555;
    --rule: #9a9a9a;
    --label: #666666;
  }
  * { margin: 0; padding: 0; box-sizing: border-box; }
  html, body { width: 805px; height: 1200px; overflow: hidden; }
  body {
    background: var(--page-bg);
    font-family: "Noto Sans JP", sans-serif;
    position: relative;
  }
  .side-label {
    position: absolute;
    left: 43px;
    font-family: "Roboto", sans-serif;
    font-size: 19px;
    color: var(--label);
  }
  .side-label--front { top: 70px; }
  .side-label--back { top: 620px; }

  .card {
    position: absolute;
    left: 43px;
    width: 716px;
    height: 448px;
    box-shadow: 0 6px 16px rgba(0,0,0,0.28);
    overflow: hidden;
  }
  .card--front {
    top: 108px;
    background: var(--card-dark);
    display: flex;
    align-items: center;
    justify-content: center;
  }
  .front-mark {
    display: flex;
    align-items: center;
    gap: 16px;
  }
  .front-mark__dot {
    width: 22px; height: 22px;
    border-radius: 50%;
    background: var(--gold);
  }
  .front-mark__name {
    font-family: "Russo One", sans-serif;
    font-size: 40px;
    color: var(--gold);
    letter-spacing: 1px;
  }

  .card--back {
    top: 668px;
    background: var(--card-light);
  }
  .back-band {
    position: absolute;
    left: 0; top: 0;
    width: 100%;
    height: 124px;
    background: var(--card-dark);
  }
  .back-band__rule {
    position: absolute;
    left: 0; top: 124px;
    width: 100%;
    height: 8px;
    background: linear-gradient(90deg, var(--gold-deep), var(--gold-light) 35%, var(--gold) 60%, var(--gold-deep));
  }
  .brand-name {
    position: absolute;
    left: 56px; top: 20px;
    font-family: "Russo One", sans-serif;
    font-size: 50px;
    line-height: 1;
    color: var(--card-light);
    letter-spacing: 1px;
  }
  .brand-tagline {
    position: absolute;
    left: 58px; top: 78px;
    font-family: "Roboto", sans-serif;
    font-weight: 700;
    font-size: 18px;
    color: var(--gold-light);
    letter-spacing: 0.5px;
  }
  .site-url {
    position: absolute;
    right: 30px; top: 90px;
    font-family: "Roboto", sans-serif;
    font-size: 17px;
    color: var(--card-light);
  }
  .person-role {
    position: absolute;
    left: 56px; top: 178px;
    font-size: 16px;
    color: var(--ink);
  }
  .person-name {
    position: absolute;
    left: 56px; top: 206px;
    display: flex;
    align-items: baseline;
    gap: 14px;
  }
  .person-name__ja {
    font-size: 30px;
    font-weight: 700;
    letter-spacing: 10px;
    color: var(--ink);
  }
  .person-name__en {
    font-family: "Roboto", sans-serif;
    font-size: 15px;
    color: var(--ink-soft);
  }
  .divider {
    position: absolute;
    left: 56px; top: 296px;
    width: 590px;
    height: 1px;
    background: var(--rule);
  }
  .contact-list {
    position: absolute;
    left: 56px; top: 318px;
    list-style: none;
  }
  .contact-list__item {
    display: flex;
    align-items: center;
    gap: 10px;
    height: 32px;
    font-size: 15px;
    color: var(--ink-soft);
  }
  .contact-icon {
    width: 20px; height: 20px;
    flex: none;
  }
</style>
</head>
<body>
  <p class="side-label side-label--front">Front</p>
  <section class="card card--front">
    <div class="front-mark">
      <span class="front-mark__dot"></span>
      <span class="front-mark__name">METRO CORE24</span>
    </div>
  </section>

  <p class="side-label side-label--back">Back</p>
  <section class="card card--back">
    <header class="back-band">
      <h1 class="brand-name">METRO CORE24</h1>
      <p class="brand-tagline">24-HOUR FITNESS GYM</p>
      <p class="site-url">https://metrocore.jp</p>
    </header>
    <div class="back-band__rule"></div>

    <p class="person-role">本町店 マネージャー</p>
    <p class="person-name">
      <span class="person-name__ja">佐藤 健一</span>
      <span class="person-name__en">Kenichi Sato</span>
    </p>
    <div class="divider"></div>

    <ul class="contact-list">
      <li class="contact-list__item">
        <svg class="contact-icon" viewBox="0 0 20 20"><rect width="20" height="20" rx="2" fill="#777"/><path d="M10 4a4 4 0 0 0-4 4c0 3 4 8 4 8s4-5 4-8a4 4 0 0 0-4-4zm0 5.5a1.5 1.5 0 1 1 0-3 1.5 1.5 0 0 1 0 3z" fill="#fff"/></svg>
        <span>〒123-4567 大阪市〇〇〇〇〇〇〇〇〇〇〇〇〇〇〇〇〇〇〇〇</span>
      </li>
      <li class="contact-list__item">
        <svg class="contact-icon" viewBox="0 0 20 20"><rect width="20" height="20" rx="2" fill="#777"/><path d="M6.5 4.5l2 2.5-1.2 1.4c.8 1.7 2 2.9 3.7 3.7l1.4-1.2 2.5 2-1.3 2c-4.5-.4-8.2-4.1-8.6-8.6z" fill="#fff"/></svg>
        <span>06-0000-0000</span>
      </li>
      <li class="contact-list__item">
        <svg class="contact-icon" viewBox="0 0 20 20"><rect width="20" height="20" rx="2" fill="#777"/><rect x="4" y="6" width="12" height="8" fill="#fff"/><path d="M4 6l6 4.5L16 6" fill="none" stroke="#777" stroke-width="1.2"/></svg>
        <span>info@example.com</span>
      </li>
    </ul>
  </section>
</body>
</html>
```